Real Estate Flyer (Brenton Property)

We need a color CMYK high resolution, print quality horizontal real estate property flyer designed in the sizes of 10" wide and 6.7425" tall and another one in 11" wide and 8.5" tall.
Ad should be professionally looking to U.S. standards. It should be sleek, modern yet classy.
We uploaded in Briefs logo files, agent photo, 2 photos of the property (Must use both) and a sample of a flyer for Vayle Morrow Luxury Residence. We like how the overlay atop the first photo in the Vayle Morrow flyer with the company logo in the overlay. We'd like to incorporate that with our logo, the background color of the overlay should match that of our logo. DON'T CHANGE LOGO COLORS. Only use two colors in ad (exact logo blue color and white). The text in the overlay must be "FOR SALE - Potential Income Producing Commercial Office Building". Other details that should be prominent underneath are "42 Brenton Dr., Schaumburg, IL 60174 - Asking Price: $650,000".
Add "Residential & Commercial" under our company logo in italic font.
Add in flyer: "Located seconds away from the Kettering Rd. & Palden Rd. Intersection"
Add in flyer:
- Completely vacant
- 10,000 sq. ft. building
- 55 Car Parking
- 1.38 acre lot
- Over 20 offices and 5 bathrooms.
- Lease out individual office spaces for great monthly cash flow
Put agent's photo and following details professionally displayed:
Dev Marlo
Managing Broker
847-555-0148
dev.marlo@qtnhomes-example.com
Add from Briefs fair housing logo and PLX logo near agent's information. Logos should be small but yet visible to understand text.
Add at bottom of the ad with separation near agent details:
Looking to Buy or Sell?
I’m your one-stop, full service licensed real estate broker.
I deal with all types of real estate properties: Homes, Condos, Townhomes, Multi-Unit Apartment Buildings and Commercial Spaces.
Let My Experience Guide You Through Every Step of the Process!
Fine print:
©2018 QTN Homes, Inc. All Rights Reserved.

```html
<!DOCTYPE html>
<html lang="en">
<head>
<meta charset="utf-8">
<title>Brenton Property – For Sale Flyer</title>
<link rel="stylesheet" href="https://fonts.googleapis.com/css2?family=Montserrat:wght@600;700&family=Open+Sans:ital,wght@0,400;0,600;1,700&display=swap">
<style>
  :root {
    --brand-blue: #0d4ea6;
    --white: #ffffff;
    --ink: #1d1d1d;
    --charcoal: #333333;
    --stage: #8f8f8f;
  }
  * { margin: 0; padding: 0; box-sizing: border-box; }
  html, body { width: 1200px; height: 1200px; overflow: hidden; background: var(--stage); }
  .flyer {
    position: absolute; left: 133px; top: 0;
    width: 1009px; height: 1297px;
    transform: scale(0.925); transform-origin: top left;
    background: var(--white); overflow: hidden;
    font-family: "Open Sans", Arial, sans-serif; color: var(--ink);
  }
  .abs { position: absolute; }
  .hero-photo {
    left: 0; top: 0; width: 1009px; height: 410px;
    background:
      linear-gradient(90deg, rgba(255,255,255,0) 0%, rgba(255,255,255,0) 45%, rgba(255,255,255,.85) 80%, #fff 100%),
      linear-gradient(180deg, #9fb4d6 0%, #c9cfd8 45%, #d9cbb6 75%, #b9a792 100%);
  }
  .brand-box {
    left: 710px; top: 29px; width: 170px; height: 143px;
    background: var(--brand-blue); display: flex; align-items: center; justify-content: center;
  }
  .brand-name { font-family: "Montserrat", sans-serif; font-weight: 700; font-size: 30px; color: var(--white); text-align: center; line-height: 1.05; }
  .brand-tagline { left: 600px; top: 180px; width: 378px; text-align: right; font-style: italic; font-weight: 700; font-size: 20px; }
  .sale-tab {
    left: 306px; top: 345px; width: 364px; height: 66px;
    background: var(--brand-blue); border-radius: 34px 34px 0 0;
    font-family: "Montserrat", sans-serif; font-weight: 700; font-size: 58px; color: var(--white);
    text-align: center; line-height: 80px; letter-spacing: 1px;
  }
  .headline-band {
    left: 0; top: 410px; width: 1009px; height: 111px; background: var(--brand-blue);
    color: var(--white); text-align: center; font-family: "Montserrat", sans-serif;
  }
  .headline-band h1 { font-size: 31px; font-weight: 700; margin-top: 15px; letter-spacing: .3px; }
  .headline-band p { font-size: 24px; font-weight: 600; margin-top: 8px; letter-spacing: .3px; }
  .location { left: 32px; top: 530px; width: 620px; }
  .location h2 { font-size: 26px; font-weight: 600; color: var(--brand-blue); line-height: 32px; }
  .location p { font-size: 16.5px; line-height: 23px; }
  .features { left: 28px; top: 618px; list-style: none; }
  .features li { font-size: 20px; height: 38.5px; display: flex; align-items: center; gap: 8px; }
  .features svg { width: 14px; height: 12px; flex: none; }
  .main-photo {
    left: 705px; top: 539px; width: 275px; height: 315px; border: 3px solid var(--brand-blue);
    background: linear-gradient(180deg, #e8c9a0 0%, #d7cfc4 40%, #b9b2a8 62%, #3b3d44 75%, #2b2c31 100%);
  }
  .pill-left {
    left: 0; top: 857px; width: 502px; height: 53px; background: var(--charcoal);
    border-radius: 0 27px 27px 0; color: var(--white);
    font-family: "Montserrat", sans-serif; font-weight: 700; font-size: 37px; line-height: 53px; padding-left: 35px;
  }
  .pitch { left: 34px; top: 918px; width: 490px; font-size: 16.5px; line-height: 23px; }
  .thumb { top: 872px; width: 219px; height: 149px; border: 2px solid var(--brand-blue); }
  .thumb-front { left: 527px; background: linear-gradient(180deg, #b9c6d6 0%, #e6c39a 40%, #6f6458 70%, #3a3b40 100%); }
  .thumb-lot { left: 761px; background: linear-gradient(180deg, #c9d2dc 0%, #8a8872 35%, #5c6a4a 48%, #2f3138 60%, #3b3d44 100%); }
  .agent-panel { left: 0; top: 1032px; width: 596px; height: 241px; background: var(--brand-blue); }
  .agent-photo { left: 20px; top: 1043px; width: 208px; height: 220px; border: 3px solid var(--white); background: linear-gradient(180deg, #f2f2f2 0%, #e2e2e2 60%, #3a3d44 100%); }
  .agent-info { left: 256px; top: 1058px; width: 330px; color: var(--white); font-weight: 600; }
  .agent-info .name { font-size: 33px; line-height: 50px; }
  .agent-info .line { font-size: 25px; line-height: 48px; }
  .agent-info .email { font-size: 18.5px; line-height: 48px; white-space: nowrap; }
  .pill-right {
    left: 605px; top: 1049px; width: 404px; height: 71px; background: var(--charcoal);
    border-radius: 36px 0 0 36px; color: var(--white); font-weight: 600; font-size: 19.5px; line-height: 27px; padding: 9px 0 0 23px;
  }
  .footer-strip {
    left: 0; top: 1280px; width: 1009px; height: 17px; background: var(--charcoal);
    color: var(--white); font-size: 10.5px; line-height: 17px; text-align: center;
  }
</style>
</head>
<body>
<main class="flyer">
  <div class="abs hero-photo" role="img" aria-label="Bright living room interior with city waterfront view through tall windows"></div>
  <div class="abs brand-box"><span class="brand-name">QTN<br>Homes</span></div>
  <p class="abs brand-tagline">Residential &amp; Commercial</p>
  <div class="abs sale-tab">FOR SALE</div>
  <header class="abs headline-band">
    <h1>Potential Income Producing Commercial Office Building</h1>
    <p>42 Brenton Dr., Schaumburg, IL 60174 - Asking Price: $650,000</p>
  </header>

  <section class="abs location">
    <h2>Location</h2>
    <p>Located seconds away from the Kettering Rd. &amp; Palden Rd.<br>Intersection</p>
  </section>
  <ul class="abs features">
    <li><svg viewBox="0 0 14 12"><path d="M0 0 L14 6 L0 12 L4 6 Z" fill="#0d4ea6"/></svg>Completely vacant</li>
    <li><svg viewBox="0 0 14 12"><path d="M0 0 L14 6 L0 12 L4 6 Z" fill="#0d4ea6"/></svg>10,000 sq. ft. building</li>
    <li><svg viewBox="0 0 14 12"><path d="M0 0 L14 6 L0 12 L4 6 Z" fill="#0d4ea6"/></svg>55 Car Parking</li>
    <li><svg viewBox="0 0 14 12"><path d="M0 0 L14 6 L0 12 L4 6 Z" fill="#0d4ea6"/></svg>1.38 acre lot</li>
    <li><svg viewBox="0 0 14 12"><path d="M0 0 L14 6 L0 12 L4 6 Z" fill="#0d4ea6"/></svg>Over 20 offices and 5 bathrooms.</li>
    <li><svg viewBox="0 0 14 12"><path d="M0 0 L14 6 L0 12 L4 6 Z" fill="#0d4ea6"/></svg>Lease out individual office spaces for great monthly cash flow</li>
  </ul>
  <div class="abs main-photo" role="img" aria-label="Two-storey office building with dormer windows beside a parking lot at sunset"></div>

  <div class="abs pill-left">Looking to Buy or Sell?</div>
  <p class="abs pitch">I’m your one-stop, full service licensed real estate broker.<br>I deal with all types of real estate properties: Homes, Condos, Townhomes, Multi-Unit Apartment Buildings and Commercial Spaces.</p>
  <div class="abs thumb thumb-front" role="img" aria-label="Front view of the office building with trees"></div>
  <div class="abs thumb thumb-lot" role="img" aria-label="Parking lot with accessible parking space"></div>

  <section class="abs agent-panel"></section>
  <div class="abs agent-photo" role="img" aria-label="Portrait of the managing broker"></div>
  <div class="abs agent-info">
    <div class="name">Dev Marlo</div>
    <div class="line">Managing Broker</div>
    <div class="line">847-555-0148</div>
    <div class="email">dev.marlo@qtnhomes-example.com</div>
  </div>
  <div class="abs pill-right">Let My Experience Guide You Through<br>Every Step of the Process!</div>

  <svg class="abs" style="left:681px;top:1195px" width="130" height="56" viewBox="0 0 130 56" role="img" aria-label="Listing service badge">
    <rect x="1" y="1" width="128" height="54" fill="none" stroke="#555" stroke-width="2"/>
  </svg>
  <svg class="abs" style="left:855px;top:1158px" width="100" height="107" viewBox="0 0 100 107" role="img" aria-label="Fair housing badge">
    <rect x="10" y="10" width="80" height="80" fill="#1d1d1d"/>
  </svg>

  <footer class="abs footer-strip">©2018 QTN Homes, Inc. All Rights Reserved.</footer>
</main>
</body>
</html>
```